Heronfield Global Trade & Heritage Link Landing Page Design

We are a Chinese high-end bespoke business travel company. We want to design a landing page, to promote our brand and business, to attract target clients for business development.

We have own logo, like design in modern simple style, like to sample as attached. Like the Sample 2, use different color to display our business services.

We want to mainly display 7 parts of business:
1. Visa Services
2. International Hotel Reservation
3. Worldwide Flight Tickets Booking
4. Worldwide Travel Arrangement
5. VIP Airport Concierge
6. Duty Free Goods
7. International Business Resources

We imagine design a world map, points out popular countries, cities, and destinations, and combine with our own business resources cities.

Design in modern, business, international style. Thank you. Look forward to cooperate with you.

Target Market(s)

Business Clients and High income private client

Industry/Entity Type

Tourism, Business Travel, International Exchange

Coding

Coded - Design and coding required

Requirements
Must have
• Our logo, large images, design a world map

```html
<!DOCTYPE html>
<html lang="en">
<head>
<meta charset="utf-8">
<title>Heronfield Global Trade &amp; Heritage Link</title>
<link href="https://fonts.googleapis.com/css2?family=Josefin+Sans:wght@400;600;700&family=Poppins:wght@500;600;700&family=Roboto:wght@400;500&display=swap" rel="stylesheet">
<style>
:root{
  --sky:#17b2d6;
  --sky-deep:#0ea3cb;
  --orange:#f59a45;
  --ink:#1c1c1c;
  --body:#444;
  --footer:#282828;
  --visa:#1f5fb0;
  --hotel:#1a9b8c;
  --flight:#7cb83a;
  --travel:#e8b412;
  --vip:#e8462a;
  --duty:#7d2a8c;
  --biz:#14a9c6;
  --pin:#e8132b;
}
*{margin:0;padding:0;box-sizing:border-box}
html,body{width:1200px;height:3701px;overflow:hidden}
body{position:relative;background:#fff;font-family:'Roboto',sans-serif;color:var(--body)}
.abs{position:absolute}

/* hero */
.hero{left:0;top:0;width:1200px;height:687px;background:linear-gradient(120deg,var(--sky) 0%,var(--sky-deep) 100%)}
.brand{display:flex;align-items:center;gap:12px}
.brand-dot{width:44px;height:44px;border-radius:50%;background:#fff}
.brand-name{font-family:'Josefin Sans',sans-serif;font-weight:700;font-size:24px;line-height:1.05;color:#fff;text-transform:uppercase}
.nav a{position:absolute;top:34px;font-family:'Roboto',sans-serif;font-size:14px;color:#fff;text-decoration:none}
.login{left:966px;top:26px;width:119px;height:38px;border-radius:19px;background:var(--orange);color:#fff;font-size:14px;font-weight:500;display:flex;align-items:center;justify-content:center;gap:8px}
.hero-title{left:111px;top:258px;font-family:'Poppins',sans-serif;font-weight:600;font-size:57px;line-height:60px;color:#fff}
.hero-text{left:111px;top:396px;width:430px;font-size:15px;line-height:26px;color:#fff}
.btn-orange{left:111px;top:468px;width:172px;height:58px;border-radius:29px;background:var(--orange);color:#fff;font-family:'Josefin Sans',sans-serif;font-weight:600;font-size:15px;letter-spacing:1px;display:flex;align-items:center;justify-content:center}
.hero-visual{left:650px;top:86px;width:500px;height:590px;border-radius:40px;background:radial-gradient(ellipse at 50% 60%,#b7774a 0%,#8f6b58 35%,rgba(60,140,170,.5) 70%,rgba(23,178,214,0) 100%)}

/* about */
.about-photo{left:114px;top:772px;width:454px;height:454px;border-radius:50%;background:linear-gradient(150deg,#c9b59a 0%,#7aa7b0 55%,#3e8f9a 100%);box-shadow:8px 6px 0 #c9cdd2}
.h2{font-family:'Josefin Sans',sans-serif;font-weight:600;color:var(--ink);letter-spacing:1.5px;text-transform:uppercase}
.about-title{left:628px;top:800px;font-size:34px;line-height:43px}
.about-text{left:628px;top:897px;width:470px;font-size:14.5px;line-height:25.7px;color:#555}
.btn-sky{left:628px;top:1121px;width:160px;height:48px;border-radius:24px;background:var(--biz);color:#fff;font-family:'Josefin Sans',sans-serif;font-weight:600;font-size:15px;letter-spacing:1px;display:flex;align-items:center;justify-content:center}

/* business */
.wash{left:0;top:1265px;width:1200px;height:1040px;background:
  radial-gradient(ellipse 420px 260px at 900px 160px,rgba(140,215,235,.55),rgba(255,255,255,0)),
  radial-gradient(ellipse 380px 300px at 250px 350px,rgba(170,170,230,.5),rgba(255,255,255,0)),
  radial-gradient(ellipse 500px 300px at 220px 750px,rgba(232,170,222,.55),rgba(255,255,255,0)),
  radial-gradient(ellipse 460px 300px at 980px 620px,rgba(200,170,230,.45),rgba(255,255,255,0))}
.biz-title{left:0;width:1200px;top:1408px;text-align:center;font-size:33px}
.biz-text{left:240px;top:1464px;width:720px;text-align:center;font-size:15px;line-height:26px;color:#444}
.ring{width:150px;height:150px;border-radius:50%;border:18px solid;display:flex;align-items:center;justify-content:center;background:#fff}
.ring-core{width:100px;height:100px;border-radius:50%;background:#fff;box-shadow:0 4px 14px rgba(0,0,0,.18);display:flex;align-items:center;justify-content:center}
.svc-label{font-family:'Josefin Sans',sans-serif;font-size:16px;line-height:24px;letter-spacing:1.2px;color:#222}
.hub{left:416px;top:1837px;width:310px;height:310px;border-radius:50%;background:#fff;box-shadow:0 8px 30px rgba(120,80,160,.12);display:flex;align-items:center;justify-content:center;flex-direction:column;gap:10px}
.hub-dot{width:56px;height:56px;border-radius:50%;background:var(--biz)}
.hub-name{font-family:'Josefin Sans',sans-serif;font-weight:700;font-size:22px;line-height:26px;color:var(--biz);text-align:center;text-transform:uppercase}

/* countries */
.map-title{left:0;width:1200px;top:2330px;text-align:center;font-size:33px}
.map{left:100px;top:2421px;width:1000px;height:440px;border-radius:30px;background:radial-gradient(ellipse at 50% 50%,#e2e4e7 0%,#f1f2f4 60%,#fff 100%)}
.pin{width:26px;height:34px}

/* testimonials */
.test-title{left:0;width:1200px;top:2961px;text-align:center;font-size:33px}
.card{top:3046px;width:307px;height:193px;background:#fff;box-shadow:0 4px 18px rgba(0,0,0,.08);padding:12px 12px}
.card-head{display:flex;align-items:center;gap:12px}
.avatar{width:60px;height:60px;border-radius:50%;background:linear-gradient(160deg,#c8ccd2,#8d939c)}
.card-name{font-family:'Poppins',sans-serif;font-weight:600;font-size:17px;color:#111}
.card-role{font-size:12px;color:#888}
.stars{margin:20px 0 0 6px;color:var(--orange);font-size:16px;letter-spacing:4px}
.card-text{margin:12px 0 0 10px;width:250px;font-size:12.5px;line-height:24px;color:#444}
.card-bar{position:absolute;right:22px;top:92px;width:6px;height:82px;border-radius:3px;background:#eee}
.card-bar i{display:block;width:6px;height:30px;margin-top:10px;border-radius:3px}
.arrow{top:3150px;font-size:22px}

/* footer */
.footer{left:0;top:3334px;width:1200px;height:367px;background:var(--footer)}
.f-head{font-family:'Josefin Sans',sans-serif;font-size:20px;letter-spacing:1.5px;color:#fff;text-transform:uppercase}
.f-text{font-size:14px;line-height:24px;color:#e6e6e6}
.f-row{display:flex;gap:10px;align-items:flex-start}
.news{left:753px;top:3449px;width:336px;height:36px;border-radius:18px;background:#fff;display:flex;align-items:center;padding-left:18px;font-size:14px;color:#777}
.news-btn{position:absolute;right:0;top:0;width:120px;height:36px;border-radius:18px;background:var(--biz);color:#fff;font-family:'Josefin Sans',sans-serif;font-weight:600;font-size:15px;display:flex;align-items:center;justify-content:center}
.social{width:12px;height:12px;border-radius:50%;background:#fff}
.f-rule{left:111px;top:3594px;width:978px;height:1px;background:#444}
</style>
</head>
<body>

<!-- HERO -->
<section class="abs hero">
  <div class="abs brand" style="left:102px;top:18px">
    <div class="brand-dot"></div>
    <div class="brand-name">Heronfield<br>Global</div>
  </div>
  <nav class="nav">
    <a style="left:514px">Home</a>
    <a style="left:601px">About Us</a>
    <a style="left:708px">Our Services</a>
    <a style="left:839px">Contact Us</a>
  </nav>
  <div class="abs login">
    <svg width="13" height="13" viewBox="0 0 14 14"><circle cx="7" cy="4" r="3.3" fill="#fff"/><path d="M1 14c0-4 3-6 6-6s6 2 6 6z" fill="#fff"/></svg>Login
  </div>
  <h1 class="abs hero-title">HERONFIELD<br>GLOBAL</h1>
  <p class="abs hero-text">Lorem ipsum dolor sit amet, consectetur adipiscing elit, sed do eiusmod tempor incididunt ut labore</p>
  <div class="abs btn-orange">GET STARTED</div>
  <div class="abs hero-visual" role="img" aria-label="Stack of travel luggage, hats and landmark towers with destination signposts"></div>
</section>

<!-- ABOUT -->
<div class="abs about-photo" role="img" aria-label="Two smiling travellers reading a city map"></div>
<h2 class="abs h2 about-title">About Heronfield<br>Global</h2>
<p class="abs about-text">Lorem ipsum dolor sit amet, consectetur adipiscing elit, sed do eiusmod tempor incididunt ut labore et dolore magna aliqua. Quis ipsum suspendisse ultrices gravida. Risus commodo viverra maecenas accumsan lacus vel facilisis. Lorem ipsum dolor sit amet, consectetur adipiscing elit, sed do eiusmod tempor incididunt ut labore et dolore magna aliqua. Quis ipsum suspendisse ultrices gravida. Risus commodo viverra maecenas accumsan lacus vel facilisis. Lorem ipsum dolor sit amet, consectetur</p>
<div class="abs btn-sky">View More</div>

<!-- BUSINESS -->
<div class="abs wash" role="img" aria-label="Soft blue and pink watercolour wash"></div>
<h2 class="abs h2 biz-title">7 Types of Business</h2>
<p class="abs biz-text">Lorem ipsum dolor sit amet, consectetur adipiscing elit, sed do eiusmod tempor incididunt ut labore et dolore magna aliqua. Quis ipsum suspendisse ultrices gravida. Risus commodo viverra maecenas accumsan lacus vel facilisis.</p>

<div class="abs hub">
  <div class="hub-dot"></div>
  <div class="hub-name">Heronfield<br>Global</div>
</div>

<div class="abs ring" style="left:225px;top:1930px;border-color:var(--visa)"><div class="ring-core">
  <svg width="40" height="28" viewBox="0 0 40 28" fill="none" stroke="var(--visa)" stroke-width="2"><rect x="1" y="1" width="38" height="26" rx="3"/><rect x="6" y="7" width="10" height="12"/><path d="M21 9h13M21 14h13M21 19h9"/></svg></div></div>
<div class="abs ring" style="left:266px;top:1790px;border-color:var(--hotel)"><div class="ring-core">
  <svg width="40" height="36" viewBox="0 0 40 36" fill="none" stroke="var(--hotel)" stroke-width="2"><rect x="2" y="12" width="36" height="22" rx="2"/><path d="M8 20h24M8 26h16"/><circle cx="20" cy="7" r="5"/><path d="M17.5 7l2 2 3-4"/></svg></div></div>
<div class="abs ring" style="left:360px;top:1681px;border-color:var(--flight)"><div class="ring-core">
  <svg width="42" height="30" viewBox="0 0 42 30" fill="none" stroke="var(--flight)" stroke-width="2"><rect x="2" y="4" width="38" height="22" rx="2" transform="rotate(-12 21 15)"/><path d="M14 17l14-6M22 10l3 9"/></svg></div></div>
<div class="abs ring" style="left:501px;top:1658px;border-color:var(--travel)"><div class="ring-core">
  <svg width="36" height="40" viewBox="0 0 36 40" fill="none" stroke="var(--travel)" stroke-width="2"><rect x="4" y="10" width="28" height="26" rx="3"/><path d="M12 10V4h12v6M4 22h28"/></svg></div></div>
<div class="abs ring" style="left:642px;top:1690px;border-color:var(--vip)"><div class="ring-core">
  <svg width="34" height="40" viewBox="0 0 34 40" fill="none" stroke="var(--vip)" stroke-width="2"><rect x="4" y="2" width="26" height="36" rx="4"/><path d="M10 12l3 7 3-7M20 12v7M24 12v7h4"/></svg></div></div>
<div class="abs ring" style="left:741px;top:1793px;border-color:var(--duty)"><div class="ring-core">
  <svg width="40" height="40" viewBox="0 0 40 40" fill="none" stroke="var(--duty)" stroke-width="2"><rect x="4" y="14" width="8" height="24" rx="2"/><path d="M6 14V8h4v6"/><path d="M16 38V18h20v20z"/><path d="M21 18v-4a5 5 0 0 1 10 0v4"/></svg></div></div>
<div class="abs ring" style="left:773px;top:1933px;border-color:var(--biz)"><div class="ring-core">
  <svg width="40" height="40" viewBox="0 0 40 40" fill="none" stroke="var(--biz)" stroke-width="2"><circle cx="20" cy="20" r="16"/><path d="M4 20h32M20 4c6 5 6 27 0 32M20 4c-6 5-6 27 0 32"/></svg></div></div>

<div class="abs svc-label" style="left:476px;top:1596px;width:200px;text-align:center">Worldwide Travel<br>Arrangement</div>
<div class="abs svc-label" style="left:200px;top:1696px">Worldwide Flight<br>Tickets Booking</div>
<div class="abs svc-label" style="left:95px;top:1816px">International<br>Hotel Reservation</div>
<div class="abs svc-label" style="left:92px;top:1953px">Visa Services</div>
<div class="abs svc-label" style="left:809px;top:1710px">VIP Airport Concierge</div>
<div class="abs svc-label" style="left:908px;top:1832px">Duty Free Goods</div>
<div class="abs svc-label" style="left:940px;top:1970px">International<br>Business Resources</div>

<!-- POPULAR COUNTRIES -->
<h2 class="abs h2 map-title">Popular Countries</h2>
<div class="abs map" role="img" aria-label="Dotted world map showing popular destinations and business resource cities"></div>
<svg class="abs" style="left:0;top:0;width:1200px;height:3701px;pointer-events:none" aria-hidden="true">
  <defs>
    <g id="pin"><path d="M0 0c-7 0-12 5-12 12 0 9 12 21 12 21s12-12 12-21c0-7-5-12-12-12z" fill="var(--pin)"/><circle cx="0" cy="12" r="4.5" fill="#fff"/></g>
  </defs>
  <use href="#pin" x="234" y="2485"/>
  <use href="#pin" x="339" y="2521"/>
  <use href="#pin" x="463" y="2428"/>
  <use href="#pin" x="645" y="2503"/>
  <use href="#pin" x="823" y="2485"/>
  <use href="#pin" x="1009" y="2449"/>
  <use href="#pin" x="559" y="2607"/>
  <use href="#pin" x="661" y="2607"/>
  <use href="#pin" x="816" y="2589"/>
  <use href="#pin" x="351" y="2661"/>
  <use href="#pin" x="405" y="2731"/>
  <use href="#pin" x="648" y="2731"/>
  <use href="#pin" x="1003" y="2747"/>
</svg>

<!-- TESTIMONIALS -->
<h2 class="abs h2 test-title">Our Testimonials</h2>
<div class="abs arrow" style="left:53px;color:var(--orange)">&#8249;</div>
<div class="abs arrow" style="left:1130px;color:var(--biz)">&#8250;</div>

<div class="abs card" style="left:111px">
  <div class="card-head"><div class="avatar"></div><div><div class="card-name">Marcus Hale</div><div class="card-role">Lorem Ipsum</div></div></div>
  <div class="stars">★★★★★</div>
  <p class="card-text">Lorem ipsum dolor sit amet, consectetur adipiscing elit, sed do eiusmod</p>
  <div class="card-bar"><i style="background:var(--biz)"></i></div>
</div>
<div class="abs card" style="left:445px">
  <div class="card-head"><div class="avatar"></div><div><div class="card-name">Lena Corvin</div><div class="card-role">Lorem Ipsum</div></div></div>
  <div class="stars">★★★★★</div>
  <p class="card-text" style="font-size:14px">I have tried other face oils before but this is the best</p>
  <div class="card-bar"><i style="background:var(--orange)"></i></div>
</div>
<div class="abs card" style="left:779px">
  <div class="card-head"><div class="avatar"></div><div><div class="card-name">Marcus Hale</div><div class="card-role">Lorem Ipsum</div></div></div>
  <div class="stars">★★★★★</div>
  <p class="card-text">Lorem ipsum dolor sit amet, consectetur adipiscing elit, sed do eiusmod</p>
  <div class="card-bar"><i style="background:var(--biz)"></i></div>
</div>

<!-- FOOTER -->
<footer class="abs footer"></footer>
<div class="abs brand" style="left:111px;top:3408px">
  <div class="brand-dot" style="background:var(--biz)"></div>
  <div class="brand-name" style="color:var(--biz);font-size:22px">Heronfield<br>Global</div>
</div>
<p class="abs f-text" style="left:111px;top:3478px;width:260px">Lorem ipsum dolor sit amet, consectetur adipiscing elit, sed do eiusmod tempor incididunt</p>

<h3 class="abs f-head" style="left:448px;top:3398px">Contact Us</h3>
<div class="abs f-row f-text" style="left:450px;top:3433px">
  <svg width="10" height="14" viewBox="0 0 10 14" style="margin-top:5px"><path d="M5 0a5 5 0 0 0-5 5c0 4 5 9 5 9s5-5 5-9a5 5 0 0 0-5-5z" fill="#fff"/><circle cx="5" cy="5" r="2" fill="var(--footer)"/></svg>
  <span>12 b Heronfield Global<br>Lorem ipsum dolor sit amet,</span>
</div>
<div class="abs f-row f-text" style="left:450px;top:3497px">
  <svg width="12" height="12" viewBox="0 0 24 24" style="margin-top:6px"><path d="M6.6 10.8a15 15 0 0 0 6.6 6.6l2.2-2.2a1 1 0 0 1 1-.25 11.4 11.4 0 0 0 3.6.57 1 1 0 0 1 1 1V20a1 1 0 0 1-1 1A17 17 0 0 1 3 4a1 1 0 0 1 1-1h3.5a1 1 0 0 1 1 1c0 1.25.2 2.45.57 3.6a1 1 0 0 1-.25 1z" fill="#fff"/></svg>
  <span>+1 555 010 2040</span>
</div>
<div class="abs f-row f-text" style="left:450px;top:3530px">
  <svg width="13" height="10" viewBox="0 0 13 10" style="margin-top:7px"><rect width="13" height="10" rx="1" fill="#fff"/><path d="M0 1l6.5 5L13 1" stroke="var(--footer)" stroke-width="1.3" fill="none"/></svg>
  <span>info@heronfieldglobal.com</span>
</div>

<h3 class="abs f-head" style="left:752px;top:3398px">Subscribe to our Newsletter</h3>
<div class="abs news">Enter Your Email<div class="news-btn">Subscribe</div></div>
<div class="abs" style="left:762px;top:3519px;display:flex;gap:18px">
  <div class="social"></div><div class="social"></div><div class="social"></div><div class="social"></div>
</div>

<div class="abs f-rule"></div>
<p class="abs f-text" style="left:109px;top:3625px">© Copyrights 2023 Heronfield Global | &nbsp;&nbsp;All Rights Reserved</p>
<p class="abs f-text" style="left:723px;top:3625px">Terms&amp;condtions | Privacy Policy | About Us Support</p>

</body>
</html>
```